Veterinary TPLO Surgery Flyer Design

Please use this flyer to make a professional-looking 1 page, double-sided client handout regarding TPLO.

You can visit our website at www.brackenfieldpetcare.com & www.northwoodsanimalsurgerygroup.com for additional logo information. The flyer should include all the text from the one provided.

Target Market(s)

Client communication to for referral surgery between sister veterinary clinics

Industry/Entity Type

Veterinary

Requirements
Must have
• The text included
Nice to have
• Nice to have the Cedar Hollow Avenue Animal CLinic & Dr. Pell Mobile vet logos incorporated.

```html
<!DOCTYPE html>
<html lang="en">
<head>
<meta charset="utf-8">
<title>TPLO Surgery Client Handout</title>
<link href="https://fonts.googleapis.com/css2?family=Inter+Tight:wght@400;500;600;700;800;900&display=swap" rel="stylesheet">
<style>
:root{
  --green-dark:#6a9a82;
  --green-mid:#88b9a2;
  --green-light:#a6d5c0;
  --box-top:#cfe6db;
  --box-bottom:#f1f8f4;
  --gray-panel:#e0e6e2;
  --ink:#1b1b1b;
  --white:#ffffff;
  --canvas:#ffffff;
}
*{box-sizing:border-box;margin:0;padding:0}
html,body{width:1200px;height:848px;overflow:hidden;background:var(--canvas)}
body{font-family:"Inter Tight",Arial,sans-serif;color:var(--ink);position:relative}
.page{position:absolute;top:56px;width:521px;height:737px;background:var(--white);overflow:hidden;box-shadow:0 1px 4px rgba(0,0,0,.18)}
.page--front{left:60px}
.page--back{left:621px}
.abs{position:absolute}
.wave{position:absolute;left:0;top:0}
.brand{position:absolute;color:var(--white);display:flex;align-items:center;gap:4px;font-weight:600;line-height:1.05}
.brand__dot{width:14px;height:14px;border-radius:50%;background:var(--white);opacity:.85;flex:none}
.brand__name{font-size:11px}
.badge{position:absolute;display:flex;flex-direction:column;align-items:center;justify-content:center;gap:3px;color:var(--white);font-weight:700;text-align:center;line-height:1.1}
.badge__circle{border-radius:50%;background:var(--white);opacity:.85}
.hero-title{left:30px;top:36px;color:var(--white);font-weight:900;font-size:36px;line-height:33px;letter-spacing:-1.4px}
.hero-by{left:29px;top:158px;color:var(--white);font-weight:700;font-size:16.5px;letter-spacing:-.6px}
.hero-sub{left:41px;top:194px;color:var(--white);font-weight:800;font-size:28px;letter-spacing:-1px;line-height:1}
.hero-sub2{left:41px;top:225px;color:var(--white);font-weight:700;font-size:15.5px;letter-spacing:-.6px}
.pill{position:absolute;height:23px;border-radius:5px;background:linear-gradient(90deg,var(--green-dark),var(--green-light));color:var(--white);font-weight:700;font-size:13.5px;letter-spacing:-.6px;padding:0 6px;display:flex;align-items:center;white-space:nowrap}
.about{left:58px;top:258px;width:396px;height:75px;background:var(--gray-panel);border-radius:0 8px 8px 0}
.about__photo{left:33px;top:254px;width:78px;height:78px;border-radius:50%;background:radial-gradient(circle at 50% 40%,#e9c9a9,#c99f74 60%,#a67b55);border:3px solid var(--white)}
.about__title{left:121px;top:262px;font-size:14px;font-weight:700;color:var(--green-dark);letter-spacing:-.6px}
.about__text{left:121px;top:280px;width:330px;font-size:7.4px;line-height:9.4px;letter-spacing:-.2px}
.body-text{font-size:8.3px;line-height:10.5px;letter-spacing:-.2px}
.figure{position:absolute;border:1.5px solid var(--green-dark)}
.figure--diagram{left:252px;top:379px;width:98px;height:86px;background:linear-gradient(160deg,#dcdad6,#c7c3c7 60%,#b9b6bb)}
.figure--xray{left:359px;top:379px;width:98px;height:86px;background:linear-gradient(180deg,#2b2b2b,#111 50%,#3a3a3a)}
.card{position:absolute;border-radius:5px;background:linear-gradient(180deg,var(--box-top),var(--box-bottom))}
.card__head{font-weight:700;font-size:10.5px;letter-spacing:-.5px}
.card__text{font-size:8.3px;line-height:10.5px;letter-spacing:-.25px;margin-top:4px}
.why-text{left:37px;top:633px;width:428px;font-size:10px;line-height:12.6px;letter-spacing:-.3px;text-align:justify}
.footer-band{left:0;top:710px;width:521px;height:27px;background:var(--green-dark)}
.footer-link{position:absolute;top:714px;color:var(--white);font-size:12.5px;font-weight:500;letter-spacing:-.2px}
.step{position:absolute;border-radius:4px;background:linear-gradient(180deg,var(--box-top),var(--box-bottom));padding:5px 6px}
.step__head{font-weight:700;font-size:8.6px;letter-spacing:-.4px}
.step__text{font-size:6.6px;line-height:8.8px;letter-spacing:-.15px;margin-top:5px;padding-left:5px;text-align:justify}
.lead{font-size:10px;line-height:12.6px;letter-spacing:-.3px}
.contact-heading{left:21px;top:596px;font-size:20px;font-weight:800;color:var(--green-dark);letter-spacing:-.9px}
.contact-col{position:absolute;top:640px;color:var(--white)}
.contact-col__title{font-size:13px;font-weight:700;line-height:15px;letter-spacing:-.6px}
.contact-list{list-style:none;margin-top:10px}
.contact-list li{display:flex;align-items:center;gap:5px;font-size:8.4px;line-height:10.4px;letter-spacing:-.2px}
.contact-list svg{width:7px;height:7px;flex:none}
</style>
</head>
<body>

<!-- FRONT SIDE -->
<section class="page page--front">
  <svg class="wave" width="521" height="300" viewBox="0 0 521 300" aria-hidden="true">
    <defs>
      <linearGradient id="frontHeader" x1="0" y1="0" x2="1" y2="1">
        <stop offset="0" stop-color="#a6d5c0"/>
        <stop offset="1" stop-color="#66957e"/>
      </linearGradient>
    </defs>
    <path d="M0,0 H521 V296 C470,250 400,240 300,238 C180,236 60,232 0,184 Z" fill="#c8e4d6"/>
    <path d="M0,0 H521 V290 C470,246 400,236 300,234 C180,232 60,228 0,180 Z" fill="url(#frontHeader)"/>
  </svg>

  <div class="brand" style="left:384px;top:27px">
    <span class="brand__dot"></span>
    <span class="brand__name">Cedar Hollow Avenue<br>Animal Clinic</span>
  </div>
  <div class="badge" style="left:422px;top:76px;width:80px;height:66px;font-size:9px">
    <span class="badge__circle" style="width:22px;height:22px"></span>
    Dr. Pell Mobile Vet
  </div>

  <h1 class="abs hero-title">ADVANCED<br>ORTHOPEDIC CARE</h1>
  <p class="abs hero-by" style="top:104px">by Dr. Rosalind Pell, DVM, DACVS-sa</p>
  <h2 class="abs hero-sub" style="top:142px">TPLO Surgery</h2>
  <p class="abs hero-sub2" style="top:168px">at Cedar Hollow Avenue Animal Clinic</p>

  <div class="abs about"></div>
  <div class="abs about__photo" role="img" aria-label="Portrait photograph of Dr. Rosalind Pell"></div>
  <h3 class="abs about__title">About Dr. Rosalind Pell</h3>
  <p class="abs about__text">Dr. Rosalind Pell is a board-certified veterinary surgeon (Diplomate of the American College of Veterinary Surgeons) with over 18 years of experience in small animal surgery. A graduate of Great Lakes State University, she completed her surgical residency at Harborview School of Veterinary Medicine. Through her mobile practice, <b>Northwoods Surgery Services</b>, Dr. Pell now provides advanced surgical procedures—such as TPLO—directly at local clinics.</p>

  <div class="pill" style="left:34px;top:353px;width:171px">What is TPLO Surgery?</div>
  <p class="abs body-text" style="left:37px;top:383px;width:205px"><b>Tibial Plateau Leveling Osteotomy (TPLO)</b> is a surgical procedure that stabilizes the stifle (knee) joint following a <b>cranial cruciate ligament (CCL)</b> rupture—a common orthopedic injury in dogs. The procedure involves altering the angle of the tibial plateau to eliminate abnormal joint motion, restoring stability and improving function.</p>
  <div class="figure figure--diagram" role="img" aria-label="Illustration of the stifle joint before and after tibial plateau leveling"></div>
  <div class="figure figure--xray" role="img" aria-label="Pre- and post-operative TPLO radiographs of a dog's tibia"></div>

  <div class="pill" style="left:34px;top:486px;width:174px">Benefits of TPLO Surgery:</div>
  <div class="card" style="left:41px;top:518px;width:135px;height:68px;padding:7px 6px 0 6px">
    <div class="card__head">• Enhanced Joint Stability:</div>
    <p class="card__text" style="padding-left:8px">Restores natural biomechanics, reducing pain and improving mobility.</p>
  </div>
  <div class="card" style="left:184px;top:518px;width:138px;height:68px;padding:7px 6px 0 8px">
    <div class="card__head">• Faster Recovery:</div>
    <p class="card__text" style="padding-left:8px">Many dogs return to normal activity faster compared to other surgical techniques.</p>
  </div>
  <div class="card" style="left:326px;top:518px;width:151px;height:68px;padding:7px 6px 0 8px">
    <div class="card__head">• Proven Long-Term Success:</div>
    <p class="card__text" style="padding-left:8px">TPLO is particularly effective in large and active breeds</p>
  </div>

  <div class="pill" style="left:34px;top:605px;width:302px">Why Choose Cedar Hollow Avenue Animal Clinic?</div>
  <p class="abs why-text">Partnering with Dr. Pell, Cedar Hollow Avenue Animal Clinic offers advanced orthopedic surgery on-site—eliminating the need for referrals or travel. This collaboration ensures your pet receives expert surgical care in a familiar, trusted environment. Our clinic works directly with your primary veterinarian to share medical records, diagnostics, and prescriptions, ensuring seamless and coordinated care for your pet</p>

  <div class="abs footer-band"></div>
  <span class="footer-link" style="left:43px">www.brackenfieldpetcare.com</span>
  <span class="footer-link" style="left:255px">www.northwoodsanimalsurgerygroup.com</span>
</section>

<!-- BACK SIDE -->
<section class="page page--back">
  <svg class="wave" width="521" height="120" viewBox="0 0 521 120" aria-hidden="true">
    <defs>
      <linearGradient id="backHeader" x1="0" y1="0" x2="1" y2="0">
        <stop offset="0" stop-color="#7fad97"/>
        <stop offset="1" stop-color="#5f8f78"/>
      </linearGradient>
    </defs>
    <path d="M0,0 H521 V114 C450,88 330,50 220,50 C130,50 50,62 0,68 Z" fill="#c8e4d6"/>
    <path d="M0,0 H521 V108 C450,82 330,44 220,44 C130,44 50,56 0,62 Z" fill="url(#backHeader)"/>
  </svg>

  <div class="brand" style="left:386px;top:16px">
    <span class="brand__dot"></span>
    <span class="brand__name">Cedar Hollow Avenue<br>Animal Clinic</span>
  </div>
  <div class="badge" style="left:440px;top:52px;width:64px;height:46px;font-size:7px">
    <span class="badge__circle" style="width:16px;height:16px"></span>
    Dr. Pell Mobile Vet
  </div>

  <div class="pill" style="left:26px;top:123px;width:410px;font-size:16px">Diagnostic Radiographs vs. TPLO Planning Radiographs</div>
  <p class="abs lead" style="left:31px;top:149px;width:440px">While diagnostic radiographs may confirm a CCL tear, <b>they are not sufficient for surgical planning.</b> TPLO requires <b>three advanced technique radiographic views</b> with precise measurements, which must be performed under sedation to reduce discomfort and allow accurate positioning</p>

  <div class="pill" style="left:26px;top:209px;width:144px;font-size:16px">Expected Process</div>

  <div class="step" style="left:21px;top:247px;width:108px;height:55px">
    <div class="step__head">1. Diagnosis:</div>
    <p class="step__text">Your pet is diagnosed with stifle instability (CCL tear) by your veterinarian.</p>
  </div>
  <div class="step" style="left:134px;top:247px;width:117px;height:64px">
    <div class="step__head">2. Referral:</div>
    <p class="step__text" style="text-align:left">Your veterinarian contacts the surgical coordinator at Cedar Hollow Avenue Animal Clinic.</p>
  </div>
  <div class="step" style="left:257px;top:247px;width:124px;height:73px">
    <div class="step__head">3. Consultation:</div>
    <p class="step__text">The coordinator contacts you to schedule a 1-hour consultation to review the procedure, estimated costs, and available surgery dates.</p>
  </div>
  <div class="step" style="left:389px;top:247px;width:116px;height:64px">
    <div class="step__head">4. Planning Radiographs:</div>
    <p class="step__text">These specialized X-rays are typically taken during the consultation under light sedation.</p>
  </div>

  <div class="step" style="left:21px;top:333px;width:108px;height:55px">
    <div class="step__head">5. Surgical Review:</div>
    <p class="step__text" style="text-align:left;letter-spacing:-.3px">Dr. Pell reviews the radiographs and your pet's medical history to confirm candidacy for TPLO.</p>
  </div>
  <div class="step" style="left:134px;top:333px;width:117px;height:72px">
    <div class="step__head">6. Deposit:</div>
    <p class="step__text">A <b>$3,500</b> deposit secures Dr. Pell's travel and surgery date. This is refundable if canceled at least <b>5 days prior</b> to the scheduled procedure.</p>
  </div>
  <div class="step" style="left:257px;top:333px;width:124px;height:55px">
    <div class="step__head">7. Surgery Day:</div>
    <p class="step__text" style="text-align:left">Your pet is dropped off in the morning and surgery is performed the same day.</p>
  </div>
  <div class="step" style="left:389px;top:333px;width:116px;height:55px">
    <div class="step__head">8. Discharge:</div>
    <p class="step__text">You'll receive a post-surgery update and your pet will go home that evening</p>
  </div>

  <div class="pill" style="left:26px;top:434px;width:250px;font-size:16px">Post-Operative Care &amp; Follow-Up</div>
  <div class="abs lead" style="left:31px;top:468px;width:460px">
    <p>Two follow-up appointments will be scheduled:</p>
    <p style="padding-left:18px">• <b>4 Weeks Post-Op:</b> Evaluate healing, refill medications, and address any questions.</p>
    <p style="padding-left:18px">• <b>8 Weeks Post-Op:</b> Sedated radiographs will confirm proper healing of the surgical site and tibia.</p>
    <p style="margin-top:12.6px">Dr. Pell will stay in direct contact with you during your pet's recovery using her custom mobile app, which allows for secure messaging and provides detailed post-operative instructions.</p>
  </div>

  <h2 class="abs contact-heading">Contact Information:</h2>
  <svg class="wave" style="top:620px" width="521" height="117" viewBox="0 0 521 117" aria-hidden="true">
    <defs>
      <linearGradient id="backFooter" x1="0" y1="0" x2="1" y2="0">
        <stop offset="0" stop-color="#6a9a82"/>
        <stop offset=".6" stop-color="#85b59f"/>
        <stop offset="1" stop-color="#a6d5c0"/>
      </linearGradient>
    </defs>
    <path d="M0,7 H390 C450,7 490,24 521,50 V117 H0 Z" fill="url(#backFooter)"/>
  </svg>

  <div class="contact-col" style="left:25px">
    <div class="contact-col__title">Cedar Hollow<br>Avenue Animal Clinic</div>
    <ul class="contact-list">
      <li><svg viewBox="0 0 10 10"><path d="M5 0.5a3.2 3.2 0 0 0-3.2 3.2C1.8 6 5 9.5 5 9.5S8.2 6 8.2 3.7A3.2 3.2 0 0 0 5 .5z" fill="#fff"/></svg>2280 Cedar Hollow Avenue, Brackenfield, MI 48990</li>
      <li><svg viewBox="0 0 10 10"><path d="M2.2 .6l1.6 2.2-1 1c.6 1.3 1.5 2.2 2.8 2.8l1-1 2.2 1.6-.8 1.9C4.4 8.9 1.1 5.6.3 1.4z" fill="#fff"/></svg>(555) 014-2087</li>
      <li><svg viewBox="0 0 10 10"><rect x=".7" y="2" width="8.6" height="6" fill="none" stroke="#fff" stroke-width="1"/><path d="M.7 2l4.3 3.5L9.3 2" fill="none" stroke="#fff" stroke-width="1"/></svg>info@brackenfieldpetcare.com</li>
      <li><svg viewBox="0 0 10 10"><circle cx="5" cy="5" r="4.3" fill="none" stroke="#fff" stroke-width=".9"/><ellipse cx="5" cy="5" rx="1.9" ry="4.3" fill="none" stroke="#fff" stroke-width=".8"/><path d="M.7 5h8.6" stroke="#fff" stroke-width=".8"/></svg>www.brackenfieldpetcare.com</li>
    </ul>
  </div>

  <div class="contact-col" style="left:251px">
    <div class="contact-col__title">Northwoods Surgery Services<br>(Dr. Rosalind Pell)</div>
    <ul class="contact-list" style="padding-left:6px">
      <li><svg viewBox="0 0 10 10"><path d="M2.2 .6l1.6 2.2-1 1c.6 1.3 1.5 2.2 2.8 2.8l1-1 2.2 1.6-.8 1.9C4.4 8.9 1.1 5.6.3 1.4z" fill="#fff"/></svg>(555) 017-3391</li>
      <li><svg viewBox="0 0 10 10"><rect x=".7" y="2" width="8.6" height="6" fill="none" stroke="#fff" stroke-width="1"/><path d="M.7 2l4.3 3.5L9.3 2" fill="none" stroke="#fff" stroke-width="1"/></svg>drpell@northwoodssurgeryservices.com</li>
      <li><svg viewBox="0 0 10 10"><circle cx="5" cy="5" r="4.3" fill="none" stroke="#fff" stroke-width=".9"/><ellipse cx="5" cy="5" rx="1.9" ry="4.3" fill="none" stroke="#fff" stroke-width=".8"/><path d="M.7 5h8.6" stroke="#fff" stroke-width=".8"/></svg>www.northwoodsanimalsurgerygroup.com</li>
    </ul>
  </div>
</section>

</body>
</html>
```